concept design for a website homepage

Hi, we are looking for a design for Homepage for our childcare centre
We want something really progressive, edgy, modern and premium. We want this website to standout but not cluttered. We only need a Homepage concept design for the below measurements.
1366 Wx768 H
The call to action is join our community
We like the idea of a split screen
Divided into 4 sections screen with the below
Locations and Enrolments
Kestrel
Careers
Partnerships
We like angles and shapes, particularly triangles in the designs in the attached examples.
Our company font is Hands of Sean
Have attached some designs that we like the look and feel of and some of our designs from our flyers and some images to use, you don't need to choose all the images, just whatever works with your design.
We have a STEM focus at our centres so something sciency would be great.
Consider in the design will be viewed on desktop and mobile phones
1 page

```html
<!DOCTYPE html>
<html lang="en">
<head>
<meta charset="utf-8">
<title>Bright Sparks – Childcare Homepage</title>
<link href="https://fonts.googleapis.com/css2?family=Caveat:wght@600;700&family=Montserrat:wght@400;500;600;700;800&display=swap" rel="stylesheet">
<style>
:root{
  --blue:#16aef4;
  --blue-light:#3cc6fd;
  --blue-deep:#0b93e4;
  --blue-royal:#1f6ff0;
  --orange:#f2552a;
  --orange-light:#f8882c;
  --yellow:#ffd21c;
  --gold:#f9c52a;
  --ink:#1d1d1f;
  --text:#4a4a4f;
  --pale:#eaf3fd;
  --white:#ffffff;
  --field:#eef1f5;
}
*{box-sizing:border-box;margin:0;padding:0}
html,body{width:1200px;height:4724px;overflow:hidden}
body{position:relative;background:var(--pale);font-family:"Montserrat",sans-serif;color:var(--text)}
.abs{position:absolute}
.script{font-family:"Caveat",cursive;font-weight:700;color:var(--ink)}
.photo{position:absolute}

/* hero */
.hero{position:absolute;left:0;top:0;width:1200px;height:752px;background:linear-gradient(180deg,var(--blue-light),var(--blue) 70%,#0ea6ef)}
.hero-blob{position:absolute;left:0;top:200px}
.logo{position:absolute;left:149px;top:0;width:126px;height:132px;background:#1598e8;border-radius:0 0 10px 10px;display:flex;align-items:center;justify-content:center;text-align:center;color:var(--yellow);font-weight:800;font-size:20px;line-height:1.1}
.nav{position:absolute;top:64px;right:132px;display:flex;gap:24px;font-size:13px;font-weight:600;color:var(--white)}
.hero-title{position:absolute;left:0;width:1200px;text-align:center;font-weight:700}
.hero-title.t1{top:205px;font-size:50px;color:var(--white)}
.hero-title.t2{top:268px;font-size:88px;color:var(--yellow);font-weight:800}
.social{position:absolute;left:124px;width:20px;height:20px;border-radius:50%;border:2px solid rgba(255,255,255,.85)}
.slides{position:absolute;left:1042px;top:282px;font-size:12px;color:rgba(255,255,255,.75);line-height:27px;font-weight:600}
.slides b{font-size:20px;color:var(--white)}
.scroll{position:absolute;left:830px;top:610px;display:flex;align-items:center;gap:10px;color:var(--white);font-size:12px;font-weight:600}
.mouse{width:14px;height:24px;border:2px solid var(--white);border-radius:8px}

.enrol{position:absolute;left:172px;top:675px;width:854px;height:160px;border-radius:22px;background:linear-gradient(180deg,var(--orange-light),var(--orange));box-shadow:0 14px 30px rgba(242,85,42,.3)}
.enrol .lead{position:absolute;left:46px;top:22px;font-family:"Caveat",cursive;font-size:34px;color:var(--white)}
.enrol .year{position:absolute;left:46px;top:54px;font-size:56px;font-weight:800;color:var(--white)}
.field{position:absolute;background:var(--white);font-size:15px;color:#555;padding-left:14px;display:flex;align-items:center;letter-spacing:.5px}
.btn-yellow{position:absolute;background:var(--yellow);color:var(--ink);font-weight:700;font-size:14px;display:flex;align-items:center;justify-content:center;letter-spacing:.5px}

/* welcome */
.h-big{position:absolute;font-weight:700;color:var(--ink);line-height:1}
.para{position:absolute;font-size:14.5px;line-height:22px;color:var(--text)}
.readmore{position:absolute;left:128px;top:1248px;font-size:13px;font-weight:700;color:var(--orange);display:flex;align-items:center;gap:8px}

/* leader */
.leader{position:absolute;left:0;top:1400px;width:1200px;height:521px;background:linear-gradient(180deg,var(--blue-light),var(--blue))}
.search{position:absolute;left:517px;top:1710px;width:523px;height:90px;background:var(--white);border-radius:8px}

/* kestrel */
.kestrel-note{position:absolute;left:600px;top:2363px;width:600px;height:81px;background:var(--white);overflow:hidden}
.kestrel-note p{position:absolute;left:0;top:0;height:81px;line-height:81px;font-size:13px;letter-spacing:1.2px;color:var(--ink);white-space:nowrap}
.kestrel-note p span{display:inline-block;height:81px;padding:0 6px 0 86px;background:var(--blue-royal);color:var(--white)}
.arrows{position:absolute;left:530px;top:2330px;width:136px;height:48px;border-radius:24px;background:linear-gradient(90deg,var(--orange),var(--orange-light));display:flex;align-items:center;justify-content:space-around;padding:0 12px}

/* careers */
.careers{position:absolute;left:0;top:2444px;width:1200px;height:510px;background:var(--white)}

/* testimonials */
.testi{position:absolute;left:0;top:2954px;width:1200px;height:692px;background:linear-gradient(180deg,var(--blue-light),var(--blue))}
.card{position:absolute;width:251px;height:268px;background:var(--white);border-radius:6px;box-shadow:0 10px 24px rgba(0,60,120,.18);overflow:hidden}
.card .stars{position:absolute;left:0;width:100%;top:36px;text-align:center;color:var(--orange-light);font-size:16px;letter-spacing:2px}
.card .quote{position:absolute;left:24px;right:24px;top:90px;font-size:12px;line-height:19px;color:var(--ink);font-weight:600}
.card .who{position:absolute;left:24px;top:196px;display:flex;align-items:center;gap:12px}
.avatar{width:46px;height:46px;border-radius:50%;background:linear-gradient(135deg,#c9b6a5,#6f5a4c)}
.who b{display:block;font-size:11.5px;color:var(--ink)}
.who small{font-size:10px;color:var(--text)}

.callbar{position:absolute;left:228px;top:3573px;width:743px;height:130px;border-radius:18px;background:linear-gradient(180deg,var(--orange-light),var(--orange));display:flex;align-items:center;justify-content:center;gap:26px;color:var(--white);box-shadow:0 14px 30px rgba(242,85,42,.3)}
.callbar .script{color:var(--white);font-size:42px}
.callbar strong{font-size:42px;font-weight:800}

/* partners */
.form-card{position:absolute;left:119px;top:3905px;width:549px;height:437px;background:var(--white);border-radius:8px}
.input{position:absolute;background:var(--field);font-size:15px;color:#666;padding-left:18px;display:flex;align-items:center}
.radio{display:inline-block;width:16px;height:16px;border-radius:50%;border:1px solid #ccc;vertical-align:middle;margin-right:8px}

/* footer */
.footer{position:absolute;left:0;top:4428px;width:1200px;height:296px;background:linear-gradient(180deg,#19b0f5,#0d9eea);color:var(--white)}
.footer h4{position:absolute;font-size:19px;font-weight:500}
.footer .loc{position:absolute;font-size:11.5px;line-height:20px}
.ficon{display:inline-block;width:24px;height:24px;border:2px solid rgba(255,255,255,.85);border-radius:50%;margin-right:18px}
</style>
</head>
<body>

<!-- HERO -->
<section class="hero">
  <svg class="hero-blob" width="1200" height="420" viewBox="0 0 1200 420" aria-hidden="true">
    <path d="M60 140 C140 40 320 60 420 100 C560 150 700 60 860 120 C960 160 960 300 860 330 C700 380 520 300 360 340 C200 380 60 300 60 140Z" fill="#0fa0ea" opacity=".35"/>
  </svg>
  <div class="logo">Bright<br>Sparks</div>
  <nav class="nav"><span>Home</span><span>About</span><span>Enrolments</span><span>Kestrel</span><span>Career</span><span>Partnerships</span><span>Contact</span></nav>
  <h1 class="hero-title t1">Laying the Foundation</h1>
  <div class="photo" role="img" aria-label="Two children in lab coats and goggles holding science beakers" style="left:300px;top:250px;width:500px;height:430px;border-radius:46% 46% 6% 6%;background:radial-gradient(ellipse at 30% 30%,#d9a98a 0,#c99a80 12%,transparent 26%),radial-gradient(ellipse at 62% 45%,#e6bba0 0,transparent 20%),radial-gradient(ellipse at 60% 88%,#f08bb8 0,transparent 28%),radial-gradient(ellipse at 85% 62%,#52c24e 0,transparent 10%),linear-gradient(180deg,#f3f3f6 0,#e8e9ee 60%,#dfe1e8 100%)"></div>
  <h2 class="hero-title t2">for Tomorrow</h2>
  <span class="social" style="top:289px"></span>
  <span class="social" style="top:328px"></span>
  <span class="social" style="top:364px"></span>
  <div class="slides"><b>01</b><br>02<br>03<br>04</div>
  <div class="scroll"><span class="mouse"></span>Scroll down for Enrolments</div>
</section>

<div class="enrol">
  <div class="lead">Enrol now for</div>
  <div class="year">2023</div>
  <div class="field" style="left:228px;top:61px;width:212px;height:38px">Your Name</div>
  <div class="field" style="left:457px;top:61px;width:212px;height:38px">Your Phone</div>
  <div class="btn-yellow" style="left:686px;top:61px;width:138px;height:38px">BOOK TOUR</div>
</div>

<!-- WELCOME -->
<div class="script abs" style="left:128px;top:918px;font-size:48px">Welcome to</div>
<h2 class="h-big" style="left:128px;top:976px;font-size:70px">Child Care</h2>
<p class="para" style="left:128px;top:1070px;width:440px">There are many variations of passages of Lorem Ipsum available, but the majority have suffered alteration in some form, by injected humour, or randomised words which don't look even slightly believable. If you are going to use a passage of Lorem Ipsum, you need to be sure there isn't anything embarrassing hidden in the middle of text. All the Lorem Ipsum generators</p>
<div class="readmore">Read More
  <svg width="28" height="10" viewBox="0 0 28 10"><path d="M0 5H26M21 1l5 4-5 4" stroke="currentColor" stroke-width="1.6" fill="none"/></svg>
</div>
<div class="photo" role="img" aria-label="Girl in lab coat and glasses holding a blue flask in front of a chemistry board" style="left:648px;top:899px;width:394px;height:428px;border-radius:14px;background:radial-gradient(ellipse at 68% 28%,#e09a6a 0,#c0703f 14%,transparent 30%),radial-gradient(ellipse at 22% 42%,#2a3fd8 0,#1b2a9e 16%,transparent 30%),radial-gradient(ellipse at 55% 80%,#e9eef5 0,#c9d6e6 30%,transparent 52%),linear-gradient(135deg,#2b4a7e,#16294f 55%,#1f3a6a)"></div>

<!-- LEADER -->
<section class="leader">
  <h2 class="h-big" style="left:517px;top:88px;font-size:58px;color:var(--white);line-height:56px">Australia’s<br>leader in childcare</h2>
  <p class="abs" style="left:517px;top:214px;width:540px;font-size:20px;line-height:32px;color:var(--white)">There are many variations of passages of Lorem Ipsum available, but the majority</p>
</section>
<div class="photo" role="img" aria-label="Boy in red overalls and orange hard hat holding a power drill" style="left:100px;top:1299px;width:313px;height:601px;border-radius:48% 48% 22% 22%;background:radial-gradient(ellipse at 52% 6%,#f58a1f 0,#e8711a 10%,transparent 16%),radial-gradient(ellipse at 50% 17%,#e2b197 0,transparent 10%),radial-gradient(ellipse at 50% 92%,#4b4b4f 0,#3a3a3d 14%,transparent 26%),linear-gradient(180deg,#f0582c 0,#e24a23 55%,#c73b1b 85%,#5a4a46 100%)"></div>
<div class="search">
  <svg class="abs" style="left:38px;top:34px;z-index:1" width="18" height="24" viewBox="0 0 18 24"><path d="M9 1C4.6 1 1 4.5 1 8.9 1 15 9 23 9 23s8-8 8-14.1C17 4.5 13.4 1 9 1z" fill="none" stroke="#555" stroke-width="1.6"/><circle cx="9" cy="9" r="3" fill="none" stroke="#555" stroke-width="1.6"/></svg>
  <div class="field" style="left:30px;top:24px;width:300px;height:44px;background:var(--field);padding-left:40px">Postal Code</div>
  <div class="btn-yellow" style="left:337px;top:24px;width:156px;height:44px">FIND LOCATION</div>
</div>

<!-- KESTREL -->
<div class="script abs" style="left:120px;top:2012px;font-size:50px">Kestrel</div>
<h2 class="h-big" style="left:120px;top:2070px;font-size:50px;line-height:49px">Towards a Smart<br>&amp; Passionate<br>Generation</h2>
<p class="para" style="left:126px;top:2238px;width:430px">There are many variations of passages of Lorem Ipsum available, but the majority have suffered alteration in some form, by injected humour, or randomised words which don't look even slightly believable.</p>
<div class="photo" role="img" aria-label="Children in lab coats gathered around a glowing volcano sand table" style="left:600px;top:1921px;width:600px;height:441px;background:radial-gradient(ellipse at 50% 82%,#f0a868 0,#d98a52 14%,transparent 34%),radial-gradient(ellipse at 40% 95%,#8fb6d6 0,transparent 30%),radial-gradient(ellipse at 25% 40%,#e6e9f0 0,#c5cbd8 12%,transparent 24%),radial-gradient(ellipse at 58% 48%,#dfe3ec 0,transparent 16%),radial-gradient(ellipse at 88% 45%,#d6dbe6 0,transparent 14%),linear-gradient(180deg,#1c2444,#2a3356 60%,#3a3f5a)"></div>
<div class="arrows">
  <svg width="34" height="14" viewBox="0 0 34 14"><path d="M34 7H2M8 1L2 7l6 6" stroke="#fff" stroke-width="2" fill="none"/></svg>
  <svg width="34" height="14" viewBox="0 0 34 14"><path d="M0 7H32M26 1l6 6-6 6" stroke="#fff" stroke-width="2" fill="none"/></svg>
</div>
<div class="kestrel-note"><p><span>We have wide range</span> of activities for children's</p></div>

<!-- CAREERS -->
<section class="careers">
  <svg class="abs" style="left:130px;top:68px" width="430" height="420" viewBox="0 0 430 420" aria-hidden="true"><path d="M60 120 C120 10 330 0 400 110 C450 200 380 330 280 380 L90 380 C30 320 20 200 60 120Z" fill="var(--gold)"/></svg>
  <div class="photo" role="img" aria-label="Smiling teacher with two schoolchildren carrying books" style="left:46px;top:42px;width:541px;height:468px;border-radius:40% 40% 0 0;background:radial-gradient(ellipse at 52% 14%,#6a4a36 0,#4a3226 9%,transparent 15%),radial-gradient(ellipse at 50% 62%,#a9b1bd 0,#8e97a6 12%,transparent 26%),radial-gradient(ellipse at 18% 75%,#7fc0e8 0,#5aa6d6 12%,transparent 24%),radial-gradient(ellipse at 80% 78%,#f6d24a 0,#efc232 12%,transparent 24%),radial-gradient(ellipse at 62% 60%,#d98a3a 0,transparent 8%)"></div>
  <div class="script abs" style="left:617px;top:88px;font-size:50px">Careers</div>
  <h2 class="h-big" style="left:617px;top:140px;font-size:50px">Happy Teachers</h2>
  <p class="para" style="left:617px;top:208px;width:462px">There are many variations of passages of Lorem Ipsum available, but the majority have suffered alteration in some form, by injected humour, or randomised words which don't look even slightly believable. If you are going to use a passage of Lorem Ipsum, you need to be sure there isn't anything embarrassing hidden in the middle of text. All the Lorem Ipsum generators</p>
  <div class="btn-yellow" style="left:618px;top:388px;width:212px;height:48px">FIND CAREER</div>
</section>

<!-- TESTIMONIALS -->
<section class="testi">
  <div class="script abs" style="left:0;width:1200px;text-align:center;top:54px;font-size:50px;color:var(--white)">Testamonial</div>
  <h2 class="h-big" style="left:0;width:1200px;text-align:center;top:120px;font-size:50px;color:var(--white)">What Parents Say</h2>

  <div class="card" style="left:125px;top:206px"><div class="stars">★★★★★</div><p class="quote">Printing and typesetting industry. Lorem Ipsum has been the industry's standard dummy text ever since the 1500s</p><div class="who"><span class="avatar" role="img" aria-label="Parent portrait"></span><div><b>Tamsin Okoro</b><small>London, Remortgage</small></div></div></div>
  <div class="card" style="left:420px;top:259px"><div class="stars">★★★★★</div><p class="quote">Printing and typesetting industry. Lorem Ipsum has been the industry's standard dummy text ever since the 1500s</p><div class="who"><span class="avatar" role="img" aria-label="Parent portrait"></span><div><b>Daniel Verhoek</b><small>London, Remortgage</small></div></div></div>
  <div class="card" style="left:716px;top:206px"><div class="stars">★★★★★</div><p class="quote">Printing and typesetting industry. Lorem Ipsum has been the industry's standard dummy text ever since the 1500s</p><div class="who"><span class="avatar" role="img" aria-label="Parent portrait"></span><div><b>Priya Castellan</b><small>London, Remortgage</small></div></div></div>
  <div class="card" style="left:1011px;top:259px"><div class="stars">★★★★★</div><p class="quote">Printing and typesetting industry. Lorem Ipsum has been the industry's standard dummy text ever since the 1500s</p><div class="who"><span class="avatar" role="img" aria-label="Parent portrait" style="background:linear-gradient(135deg,#f06a8c,#b0304f)"></span><div><b>Tamsin Okoro</b><small>London, Remortgage</small></div></div></div>
</section>

<div class="callbar"><span class="script">Calle Us for Info</span><strong>+61 100 200 300</strong></div>

<!-- PARTNERS -->
<div class="script abs" style="left:0;width:1200px;text-align:center;top:3742px;font-size:50px">Partners</div>
<h2 class="h-big" style="left:0;width:1200px;text-align:center;top:3812px;font-size:38px;font-weight:600">Like to Join The Our Family?</h2>
<div class="form-card">
  <div class="input" style="left:28px;top:56px;width:234px;height:46px">Full Name</div>
  <div class="input" style="left:279px;top:56px;width:234px;height:46px">Phone Number</div>
  <div class="input" style="left:28px;top:123px;width:485px;height:46px">Email Address</div>
  <div class="abs" style="left:28px;top:204px;font-size:15px;font-weight:600;color:var(--ink)">Perfect Contact method</div>
  <div class="abs" style="left:262px;top:204px;font-size:15px;color:#666"><span class="radio"></span>Phone</div>
  <div class="abs" style="left:380px;top:204px;font-size:15px;color:#666"><span class="radio"></span>Email</div>
  <div class="input" style="left:28px;top:257px;width:485px;height:90px;align-items:flex-start;padding-top:18px">Phone Number</div>
</div>
<div class="photo" role="img" aria-label="Boy in lab coat holding a beaker of red liquid" style="left:688px;top:4090px;width:367px;height:338px;border-radius:46% 46% 0 0;background:radial-gradient(ellipse at 55% 20%,#3a2a22 0,#2a1d18 12%,transparent 22%),radial-gradient(ellipse at 55% 34%,#a87458 0,transparent 14%),radial-gradient(ellipse at 22% 62%,#b5372a 0,#8f2a20 8%,transparent 14%),radial-gradient(ellipse at 55% 82%,#e07a3a 0,#c9652c 16%,transparent 32%),linear-gradient(180deg,#f4f4f6 0,#e9e9ee 100%)"></div>

<!-- FOOTER -->
<footer class="footer">
  <h4 style="left:123px;top:60px">Call us Any Time</h4>
  <div class="abs" style="left:123px;top:86px;font-size:30px;font-weight:800;color:var(--yellow)">+44 100 200 300</div>
  <div class="abs" style="left:123px;top:136px"><span class="ficon"></span><span class="ficon"></span><span class="ficon"></span><span class="ficon"></span></div>
  <h4 style="left:422px;top:60px">Head Office</h4>
  <div class="abs" style="left:422px;top:88px;font-size:15px;line-height:19px">27 Harbourview Lane<br>Lumen Bay, Lakeshire<br>LB4 2QX</div>
  <h4 style="left:662px;top:56px">Locations</h4>
  <div class="loc" style="left:662px;top:96px">Ashvale, NSW (coming soon)<br>Brookfield (coming soon)<br>Cedar Point, NSW (coming soon)<br>Dunmore River L, QLD<br>Dunmore River 2, QLD<br>Eastwick/Fernvale, QLD</div>
  <div class="loc" style="left:870px;top:96px">Fernhill, NSW<br>Glenrowan, NSW<br>Hollybank, NSW<br>Ivywood, NSW<br>Willowmere Junior &amp; Preschool, NSW<br>Juniper Hill (Acorn Grove Pre-School)</div>
  <div class="abs" style="left:0;width:1200px;text-align:center;top:248px;font-size:10px">Copyright © 2010-2021 your company name</div>
</footer>

</body>
</html>
```